Wendorf Legal: Sole Practitioner Law Firm seeking corporate branding drawing on unique bush setting

I need a logo, stationary and business card design for my law firm. I will be practising as a sole practitioner specialising in corporate, commercial, finance, migration and agriculture law. Having left my corporate job in the city and relocated our family to our farm in regional Western Australia, I would like the corporate design for my company to be crisp, stylish, concise and uncomplicated. The law firm is called "Wendorf Legal" because we have a colony of the endangered Carnaby Black Cockatoos living in the bush behind our homestead (which is also my office). I will travel to clients rather than have them visit me. I would like to see a stylised image of the bird with some Australian native bush included in the design, either as a background image on the back of the card. A separate brief has been created for the logo and stationary though I hope all 3 pieces of work will "marry". The final design should communicate clarity of vision, efficiency, compassion and solution/ outcome focused. I prefer to have the business cards printed on card with a bit of texture and substance. I will try not to use laminated card as I consider it feels "plastic and commoditised" which is inconsistent with the image and feel of the business I intend creating. Please see attached brief for further details of the design brief.

Target Market(s)

Agriculture and Horticulture companies, Farmers, Family offices and estates, banks, insurance companies, individuals wishing to migrate to Australia

Industry/Entity Type

Legal

Contact Information for Business Card

Harriet Dunbar-Kelso
LLB (Hons), BSc., MEc.
Legal Practitioner and Director

WENDORF LEGAL PTY LTD
PO Box 273, Yarrowind WA 6057
Ph: 0472 918205
Email: harrietdk@quillnet.com

Solicitor admitted to practice in the Senior Bench Tribunal of Western Australia, England and Wales, NSW, and Registered Practitioner of the Apex Bench of Australia

Logo Text

WENDORF LEGAL: Client Focused Commercial Legal Solutions

Font styles to use
Other font styles liked:
• Verlag

Colors
ec1f27
fbee3d
9bcb3c
ffffff
1b1b1b
c4c4c4

Requirements
Must have
• A look and feel of quality, conservatism, adventure
Nice to have
• A stylised image of a Carnaby Cockatoo and Australian flora as a background image or design on the back of the card.
Should not have
• Clutter, cartoons

```html
<!DOCTYPE html>
<html lang="en">
<head>
<meta charset="utf-8">
<title>Wendorf Legal – Business Card</title>
<link rel="stylesheet" href="https://fonts.googleapis.com/css2?family=Cinzel:wght@400;600&family=Open+Sans:wght@400;600&display=swap">
<style>
  :root {
    --backdrop: #1b1b1b;
    --card-deep: #1f2a1a;
    --card-mid: #3b4a2c;
    --card-warm: #4d4630;
    --band: #151515;
    --silver: #c4c4c4;
    --silver-bright: #e2e2e2;
  }
  html, body {
    margin: 0;
    width: 1200px;
    height: 1200px;
    overflow: hidden;
    background: var(--backdrop);
  }
  .business-card {
    position: absolute;
    left: 150px;
    top: 310px;
    width: 900px;
    height: 580px;
    border-radius: 18px;
    overflow: hidden;
    color: var(--silver);
    font-family: "Open Sans", Arial, sans-serif;
  }
  .bush-backdrop {
    position: absolute;
    inset: 0;
    background:
      radial-gradient(ellipse at 30% 25%, var(--card-warm) 0%, transparent 55%),
      radial-gradient(ellipse at 70% 75%, var(--card-mid) 0%, transparent 60%),
      linear-gradient(135deg, var(--card-mid), var(--card-deep));
  }
  .holder-name {
    position: absolute;
    right: 50px;
    top: 60px;
    margin: 0;
    font-family: "Cinzel", Georgia, serif;
    font-weight: 400;
    font-size: 40px;
    letter-spacing: 1px;
    color: var(--silver-bright);
  }
  .holder-credentials {
    position: absolute;
    right: 50px;
    top: 125px;
    margin: 0;
    text-align: right;
    font-size: 22px;
    line-height: 1.5;
  }
  .brand-mark {
    position: absolute;
    left: 60px;
    top: 245px;
    width: 110px;
    height: 110px;
    background: var(--silver);
  }
  .brand-band {
    position: absolute;
    left: 200px;
    right: 0;
    top: 225px;
    height: 150px;
    background: var(--band);
    opacity: 0.92;
  }
  .brand-name {
    position: absolute;
    left: 30px;
    top: 22px;
    margin: 0;
    font-family: "Cinzel", Georgia, serif;
    font-weight: 400;
    font-size: 52px;
    letter-spacing: 2px;
    color: var(--silver-bright);
    white-space: nowrap;
  }
  .brand-entity {
    position: absolute;
    left: 30px;
    right: 30px;
    top: 92px;
    display: flex;
    align-items: center;
    gap: 16px;
    font-family: "Cinzel", Georgia, serif;
    font-size: 24px;
    letter-spacing: 3px;
    color: var(--silver-bright);
  }
  .brand-entity::before,
  .brand-entity::after {
    content: "";
    flex: 1;
    height: 2px;
    background: var(--silver);
  }
  .postal-address {
    position: absolute;
    right: 50px;
    top: 410px;
    margin: 0;
    font-size: 24px;
  }
  .contact-line {
    position: absolute;
    left: 50px;
    right: 50px;
    top: 470px;
    margin: 0;
    font-size: 24px;
    text-align: right;
    white-space: nowrap;
  }
</style>
</head>
<body>
  <article class="business-card">
    <div class="bush-backdrop" role="img" aria-label="Photograph of Australian native bush with grevillea flowers and foliage"></div>
    <h1 class="holder-name">Harriet Dunbar-Kelso</h1>
    <p class="holder-credentials">LLB (Hons), BSc., MEc.<br>Legal Practitioner and Director</p>
    <div class="brand-mark"></div>
    <div class="brand-band">
      <p class="brand-name">WENDORF LEGAL</p>
      <div class="brand-entity">PTY LTD</div>
    </div>
    <p class="postal-address">PO Box 273, Yarrowind WA 6057</p>
    <p class="contact-line">T: 0472 918205 | E: harrietdk@quillnet.com</p>
  </article>
</body>
</html>
```